Indy Film Production Company/Studio

We need a business card designed from an existing logo. We are a digital studio/production company that caters to creating genre entertainment, like Action, Horror, and martial arts. The card along with the logo will be used to Brand the company from letter heads to banners. The design will also be used for postcards and Brochures. It should be professional and masculine.
Updates

Thank you to all the designers who have participated. I'm narrowing down who it will be. Thank you again.

Target Market(s)

Investors, Networks, Producers, and actors

Industry/Entity Type

Film Production

Contact Information for Business Card

Benedict Harlowe
Producer/Writer/Director
www.pelvarmotionworks.com

Requirements
Must have
• Website address, plain circle icon and plain circle icon possibly in the back of the card.
Nice to have
• Logline of Company: Follow The Action.

```html
<!DOCTYPE html>
<html lang="en">
<head>
<meta charset="UTF-8">
<title>Pelvar Motion Works – Business Card</title>
<link rel="stylesheet" href="https://fonts.googleapis.com/css2?family=Saira+Semi+Condensed:wght@500;700&family=Titillium+Web:wght@400&display=swap">
<style>
  :root {
    --backdrop: #d8d3cd;
    --card: #ecebe8;
    --brand-red: #c8121c;
    --brand-red-deep: #8e0a10;
    --ink: #2a2a2a;
    --stripe: #161616;
    --light-text: #f1e9e9;
  }
  html, body {
    margin: 0;
    width: 1200px;
    height: 969px;
    overflow: hidden;
    background: var(--backdrop);
  }
  .card {
    position: absolute;
    left: 100px;
    top: 200px;
    width: 1000px;
    height: 568px;
    background: var(--card);
    overflow: hidden;
    box-shadow: 0 10px 30px rgba(0,0,0,0.18);
  }
  .card-art {
    position: absolute;
    inset: 0;
  }
  .brand {
    position: absolute;
    left: 46px;
    top: 46px;
    margin: 0;
    color: var(--brand-red);
    font-family: "Saira Semi Condensed", sans-serif;
    font-weight: 700;
    line-height: 0.95;
  }
  .brand-main {
    display: block;
    font-size: 116px;
    letter-spacing: 2px;
  }
  .brand-sub {
    display: block;
    font-size: 40px;
    letter-spacing: 1px;
  }
  .person-name {
    position: absolute;
    left: 48px;
    top: 266px;
    margin: 0;
    font-family: "Saira Semi Condensed", sans-serif;
    font-weight: 500;
    font-style: italic;
    font-size: 36px;
    color: var(--brand-red);
    letter-spacing: 0.5px;
  }
  .person-role {
    position: absolute;
    left: 48px;
    top: 314px;
    margin: 0;
    font-family: "Saira Semi Condensed", sans-serif;
    font-weight: 500;
    font-style: italic;
    font-size: 25px;
    color: var(--ink);
  }
  .social {
    position: absolute;
    left: 835px;
    top: 350px;
    display: flex;
    gap: 8px;
  }
  .social-dot {
    width: 46px;
    height: 46px;
    border: 2px solid var(--light-text);
    border-radius: 50%;
    box-sizing: border-box;
  }
  .contact {
    position: absolute;
    right: 24px;
    top: 414px;
    margin: 0;
    padding: 0;
    list-style: none;
    font-family: "Titillium Web", sans-serif;
    font-size: 25px;
    color: var(--light-text);
    text-align: right;
  }
  .contact li {
    display: flex;
    justify-content: flex-end;
    align-items: center;
    gap: 12px;
    height: 39px;
  }
  .contact svg {
    width: 24px;
    height: 24px;
    fill: var(--light-text);
  }
</style>
</head>
<body>
  <div class="card">
    <svg class="card-art" viewBox="0 0 1000 568" aria-hidden="true">
      <defs>
        <linearGradient id="red-panel" x1="0" y1="0" x2="1" y2="1">
          <stop offset="0" stop-color="var(--brand-red)"/>
          <stop offset="1" stop-color="var(--brand-red-deep)"/>
        </linearGradient>
      </defs>
      <polygon points="412,568 938,0 1000,0 1000,10 432,568" fill="var(--stripe)"/>
      <polygon points="442,568 1000,24 1000,568" fill="url(#red-panel)"/>
    </svg>

    <h1 class="brand">
      <span class="brand-main">PELVAR</span>
      <span class="brand-sub">MOTION WORKS</span>
    </h1>

    <p class="person-name">BENEDICT HARLOWE</p>
    <p class="person-role">PRODUCER/WRITER/DIRECTOR</p>

    <div class="social">
      <span class="social-dot"></span>
      <span class="social-dot"></span>
    </div>

    <ul class="contact">
      <li>555 0142 7788
        <svg viewBox="0 0 24 24"><path d="M6.6 10.8a15 15 0 0 0 6.6 6.6l2.2-2.2a1 1 0 0 1 1-.25 11.4 11.4 0 0 0 3.6.57 1 1 0 0 1 1 1V20a1 1 0 0 1-1 1A17 17 0 0 1 3 4a1 1 0 0 1 1-1h3.5a1 1 0 0 1 1 1c0 1.25.2 2.45.57 3.57a1 1 0 0 1-.25 1z"/></svg>
      </li>
      <li>hello@pelvarmotionworks.com
        <svg viewBox="0 0 24 24"><path d="M2 5h20v14H2z M3.5 6.5 12 13l8.5-6.5" fill="var(--light-text)"/><path d="M3 6l9 7 9-7" fill="none" stroke="#a30d14" stroke-width="1.6"/></svg>
      </li>
      <li>www.pelvarmotionworks.com
        <svg viewBox="0 0 24 24"><circle cx="12" cy="12" r="10"/><path d="M2 12h20M12 2c3 3 3 17 0 20M12 2c-3 3-3 17 0 20" fill="none" stroke="#a30d14" stroke-width="1.4"/></svg>
      </li>
    </ul>
  </div>
</body>
</html>
```